依頼概要
■依頼の目的/概要
遊技業組合のポスターデザインの制作をお願いします。
パチンコ店の出玉を換金せずにお楽しみ袋と交換して家に持ち帰ってもらうよう呼びかけるポスターです。。
カウンター前にお楽しみ袋が積まれたワゴンを設置(添付PDF)
店内にポスターを貼ります。

■依頼詳細
過去の制作は26年1月はポスター。26年12月はPOPスタンドパネル。27年はのぼり、昨年28年12月はポスターを制作。
http://www.hanamizu-kumiai.jp/event/index.cgi

・パチンコ・スロットのホール内に掲示します。
・ホール内で目につくカラー・デザインをお願いします。
・社会を風刺作品や今年の流行をとり入れていただくなど。

■原稿内容
・カラー B2ポスター
・景品持ち帰り推進運動
・平成29年12月16日(土)~平成29年1月24日(日)
・山並遊興事業協同組合
コピーはお任せいたします。

その他何かご不明な点がございましたら、お気軽にご質問下さい。
よろしくお願いいたします。
■ 選んだ理由

大変お待たせしました。
どのデザインも好評でしたが目に留まることで選ばれました。
ありがとうございました。 森下

■ 提案者全員のお礼・コメント

たくさんの提案ありがとうございました。
ありがとうございました。 森下

```html
<!DOCTYPE html>
<html lang="ja">
<head>
<meta charset="utf-8">
<title>景品持ち帰り推進運動</title>
<link href="https://fonts.googleapis.com/css2?family=Noto+Sans+JP:wght@700;900&family=Noto+Serif+JP:wght@600;900&display=swap" rel="stylesheet">
<style>
  :root {
    --paper: #ffffff;
    --ink: #222222;
    --red: #e60012;
    --green: #2b9b3b;
    --crowd-a: #f6c6a8;
    --crowd-b: #cfe3f2;
    --crowd-c: #f3e3a6;
  }
  html, body { margin: 0; padding: 0; overflow: hidden; }
  .poster {
    position: relative;
    width: 849px;
    height: 1200px;
    background: var(--paper);
    overflow: hidden;
    font-family: "Noto Serif JP", serif;
    color: var(--ink);
  }
  .crowd {
    position: absolute;
    border-radius: 40px;
    opacity: 0.85;
  }
  .crowd--left {
    left: 0; top: 0; width: 440px; height: 1130px;
    border-radius: 0 60px 60px 0;
    background: linear-gradient(160deg, var(--crowd-b), var(--crowd-a) 45%, var(--crowd-c) 80%, var(--crowd-b));
  }
  .crowd--right {
    right: 0; top: 990px; width: 420px; height: 140px;
    border-radius: 60px 0 0 0;
    background: linear-gradient(90deg, var(--crowd-c), var(--crowd-a));
  }
  .copy {
    position: absolute;
    right: 28px;
    margin: 0;
    text-align: right;
    font-weight: 600;
    font-size: 25px;
    line-height: 1;
    white-space: nowrap;
  }
  .copy--shout {
    color: var(--red);
    font-family: "Noto Sans JP", sans-serif;
    font-weight: 900;
  }
  .headline-number {
    position: absolute;
    left: 110px; top: 360px;
    margin: 0;
    font-family: "Noto Sans JP", sans-serif;
    font-weight: 900;
    font-size: 200px;
    line-height: 1;
    letter-spacing: -6px;
    color: var(--red);
  }
  .count {
    position: absolute;
    right: 40px; top: 665px;
    margin: 0;
    font-family: "Noto Sans JP", sans-serif;
    font-weight: 900;
    font-size: 108px;
    line-height: 1;
    color: var(--red);
  }
  .campaign {
    position: absolute;
    right: 40px; top: 790px;
    margin: 0;
    text-align: center;
    font-family: "Noto Sans JP", sans-serif;
    font-weight: 900;
    color: var(--green);
    font-size: 58px;
    line-height: 1.1;
  }
  .dates {
    position: absolute;
    right: 30px; top: 938px;
    margin: 0;
    font-family: "Noto Sans JP", sans-serif;
    font-weight: 700;
    font-size: 24px;
    line-height: 1.35;
    color: var(--ink);
    text-align: left;
  }
  .dates span { color: var(--red); }
  .org-band {
    position: absolute;
    left: 0; bottom: 0;
    width: 100%; height: 70px;
    background: var(--green);
    display: flex; align-items: center; justify-content: flex-end;
  }
  .org-name {
    margin: 0 40px 0 0;
    color: var(--paper);
    font-weight: 600;
    font-size: 28px;
    letter-spacing: 2px;
  }
</style>
</head>
<body>
<div class="poster">
  <div class="crowd crowd--left" role="img" aria-label="笑顔で手を振る大勢の人々のイラストが数字の形に並ぶ群衆"></div>
  <div class="crowd crowd--right" role="img" aria-label="下部に並ぶ家族や人々のイラスト"></div>

  <p class="copy" style="top:38px">みんな、今日はどうだった</p>
  <p class="copy copy--shout" style="top:80px;font-size:46px">はぁ〜!</p>
  <p class="copy" style="top:145px">いっぱい楽しんだんじゃない?</p>
  <p class="copy" style="top:188px">家族をわすれ、遊技を楽しんだハッピータイム!</p>
  <p class="copy copy--shout" style="top:240px;font-size:36px">ヨッ!!、ストレスしらず!!</p>
  <p class="copy" style="top:292px">じゃ景品お持ち帰り…。</p>
  <p class="copy" style="top:332px">…だって、地球上で待ってる人</p>

  <p class="headline-number">35億</p>

  <p class="copy" style="top:582px">ちょっと無理!</p>
  <p class="copy" style="top:624px">…でも、自宅には笑顔が</p>

  <p class="count">35回</p>
  <h1 class="campaign">景品持ち帰り<br>推進運動</h1>
  <p class="dates">平成29年12月16日(土)<span>▶</span><br>平成30年1月21日(日)</p>

  <footer class="org-band">
    <p class="org-name">山並遊興事業協同組合</p>
  </footer>
</div>
</body>
</html>
```